Velvet Harbour Entertainment

We would like a design to fit on a retractable cloth banner
size - 590mm x 1490mm

We want to promote our live music business at expos (weddings, corporate events and private parties are our bread and butter)

Our focus is Jazz and Classical music - although we offer rock/pop/contemporary also

We need our contacts on there also - i'm happy to go with what you suggest

email: velvet_harbour@quillnet.example
mob: 0498 315 274
web: www.velvetharbour.example.au

Target Market(s)

Live Music for:
Corporate Events
Weddings
Private Parties

Industry/Entity Type

Events

Font styles to use
Serif
Sans Serif

Colors
f78f20

Requirements
Must have
• Would love you to pic appropriate shots from our website at http://www.velvetharbour.example.au

if you need better resolution sent through please let me know and i will upload

```html
<!DOCTYPE html>
<html lang="en">
<head>
<meta charset="utf-8">
<title>Velvet Harbour Entertainment – Expo Banner</title>
<link rel="stylesheet" href="https://fonts.googleapis.com/css2?family=Arvo&family=Josefin+Sans:wght@400&family=Oleo+Script:wght@700&family=Rokkitt:wght@400;500&display=swap">
<style>
  :root {
    --orange: #f78f20;
    --charcoal: #2b2828;
    --charcoal-deep: #222020;
    --white: #ffffff;
    --circle: #e4e3e1;
    --ink: #1f1d1d;
    --page: #ece9e5;
  }
  * { margin: 0; padding: 0; box-sizing: border-box; }
  html, body { width: 1200px; height: 675px; overflow: hidden; background: var(--page); }
  .banner {
    position: absolute; left: 470px; top: 10px;
    width: 260px; height: 655px; overflow: hidden;
    background: var(--charcoal);
  }
  .banner-shapes { position: absolute; inset: 0; }
  .brand {
    position: absolute; left: 0; top: 0; width: 260px; height: 113px;
    display: flex; flex-direction: column; justify-content: center; align-items: flex-end;
    padding-right: 16px;
    font-family: "Josefin Sans", sans-serif; font-weight: 400; color: var(--white);
    text-align: right; line-height: 1.05;
  }
  .brand-name { font-size: 25px; }
  .brand-sub { font-size: 13px; letter-spacing: 3.5px; margin-top: 4px; }
  .tagline {
    position: absolute; left: 0; top: 113px; width: 260px; height: 55px;
    background: var(--white); color: var(--ink);
    font-family: "Rokkitt", serif; font-size: 18px; font-weight: 500;
    display: flex; align-items: center; justify-content: center;
  }
  .genres {
    position: absolute; left: 6px; top: 188px; width: 260px;
    transform: rotate(-5deg); transform-origin: left center;
    color: var(--white); white-space: nowrap;
    text-shadow: 1px 1px 2px rgba(0,0,0,0.35);
  }
  .genre-script { font-family: "Oleo Script", cursive; font-weight: 700; font-size: 22px; }
  .genre-caps { font-family: "Rokkitt", serif; font-variant: small-caps; font-size: 24px; margin: 0 6px; position: relative; top: 6px; }
  .genre-dance { position: relative; top: -4px; }
  .contact {
    position: absolute; left: 8px; height: 22px;
    display: flex; align-items: center; gap: 8px;
    transform: rotate(-5.5deg); transform-origin: left center;
    font-family: "Arvo", serif; font-size: 11px; color: var(--white); white-space: nowrap;
  }
  .contact-icon { width: 21px; height: 21px; flex: none; }
  .contact--email { top: 259px; }
  .contact--phone { top: 300px; }
  .contact--web { top: 341px; }
  .book-now {
    position: absolute; right: 6px; top: 350px;
    transform: rotate(-7deg); transform-origin: right center;
    font-family: "Rokkitt", serif; font-size: 15px; color: var(--white);
  }
  .gallery { position: absolute; left: 0; top: 375px; width: 260px; height: 280px; }
  .photo { position: absolute; }
  .photo--violin { left: 0; top: 0; width: 128px; height: 92px; background: linear-gradient(135deg, #7a4a2a, #c7894f 55%, #3a2a22); }
  .photo--ensemble { left: 131px; top: 0; width: 129px; height: 47px; background: linear-gradient(90deg, #d8d8d8, #6d6d6d 50%, #bdbdbd); }
  .photo--keys { left: 0; top: 95px; width: 128px; height: 72px; background: linear-gradient(160deg, #3a1f22, #8a6a6c 55%, #2a1618); }
  .photo--hall { left: 131px; top: 50px; width: 129px; height: 117px; background: linear-gradient(180deg, #e6e6e6, #8c8c8c 60%, #3c3c3c); }
  .photo--microphone { left: 0; top: 170px; width: 128px; height: 110px; background: linear-gradient(180deg, #9a8066, #d9c2a0 50%, #5e4a3a); }
  .photo--duo { left: 131px; top: 170px; width: 129px; height: 110px; background: linear-gradient(135deg, #c9a574, #6b4324 55%, #2e1e16); }
  .gallery-label {
    position: absolute; width: 60px; height: 60px; border-radius: 50%;
    background: var(--circle); color: var(--ink);
    display: flex; align-items: center; justify-content: center; text-align: center;
    font-family: "Arvo", serif; font-size: 10px; line-height: 1.25;
  }
  .gallery-label--wedding { left: 61px; top: 27px; }
  .gallery-label--corporate { left: 201px; top: 88px; }
  .gallery-label--private { left: 60px; top: 204px; }
</style>
</head>
<body>
  <main class="banner">
    <svg class="banner-shapes" width="260" height="655" viewBox="0 0 260 655" aria-hidden="true">
      <polygon points="0,168 260,168 260,225 0,250" fill="#f78f20"/>
      <polygon points="0,250 260,225 260,229 0,254" fill="#1a1818" opacity="0.6"/>
      <line x1="0" y1="292" x2="260" y2="267" stroke="#1a1818" stroke-width="3"/>
      <line x1="0" y1="294" x2="260" y2="269" stroke="#3a3636" stroke-width="1"/>
      <line x1="0" y1="333" x2="260" y2="308" stroke="#1a1818" stroke-width="3"/>
      <line x1="0" y1="335" x2="260" y2="310" stroke="#3a3636" stroke-width="1"/>
      <polygon points="0,375 260,342 260,375" fill="#f78f20"/>
    </svg>

    <header class="brand">
      <span class="brand-name">Velvet Harbour</span>
      <span class="brand-sub">ENTERTAINMENT</span>
    </header>

    <p class="tagline">Book Distinctive Live Music</p>

    <p class="genres">
      <span class="genre-script">Jazz</span><span class="genre-caps">Classical</span><span class="genre-script genre-dance">Dance</span>
    </p>

    <p class="contact contact--email">
      <svg class="contact-icon" viewBox="0 0 22 22" aria-hidden="true"><circle cx="11" cy="11" r="11" fill="#f78f20"/><rect x="5.5" y="7.5" width="11" height="7.5" fill="none" stroke="#2b2828" stroke-width="1.6"/><polyline points="5.5,7.5 11,12 16.5,7.5" fill="none" stroke="#2b2828" stroke-width="1.6"/></svg>
      <span>velvet_harbour@quillnet.example</span>
    </p>
    <p class="contact contact--phone">
      <svg class="contact-icon" viewBox="0 0 22 22" aria-hidden="true"><circle cx="11" cy="11" r="11" fill="#f78f20"/><path d="M7 5.5c1 0 1.6 2.2 1.6 2.8s-1 1-1 1.4c.5 1.6 1.9 3 3.5 3.6.4 0 .8-1 1.4-1s2.8.6 2.8 1.6-1.4 2.3-2.6 2.2C9 15.6 6.3 12.9 5.9 8.1 5.8 6.9 6 5.5 7 5.5z" fill="#2b2828"/></svg>
      <span>0498 315 274</span>
    </p>
    <p class="contact contact--web">
      <svg class="contact-icon" viewBox="0 0 22 22" aria-hidden="true"><circle cx="11" cy="11" r="11" fill="#f78f20"/><g fill="none" stroke="#2b2828" stroke-width="1.2"><circle cx="11" cy="11" r="6"/><ellipse cx="11" cy="11" rx="2.6" ry="6"/><line x1="5" y1="11" x2="17" y2="11"/><line x1="6" y1="8" x2="16" y2="8"/><line x1="6" y1="14" x2="16" y2="14"/></g></svg>
      <span>www.velvetharbour.example.au</span>
    </p>

    <p class="book-now">Book Now</p>

    <section class="gallery">
      <div class="photo photo--violin" role="img" aria-label="Photo of a violinist performing"></div>
      <div class="photo photo--ensemble" role="img" aria-label="Black and white photo of musicians in suits with drums and double bass"></div>
      <div class="photo photo--keys" role="img" aria-label="Close-up photo of piano keys"></div>
      <div class="photo photo--hall" role="img" aria-label="Black and white photo of a double bass silhouette in a lit event hall"></div>
      <div class="photo photo--microphone" role="img" aria-label="Photo of a vintage stage microphone"></div>
      <div class="photo photo--duo" role="img" aria-label="Photo of a pianist and double bass player performing"></div>
      <p class="gallery-label gallery-label--wedding">Wedding<br>Music</p>
      <p class="gallery-label gallery-label--corporate">corporate<br>events</p>
      <p class="gallery-label gallery-label--private">private<br>parties</p>
    </section>
  </main>
</body>
</html>
```